Vértice Solar needs the best stationery in the development business

We need a stationary design for a new company based in Porto, Portugal. We are a new property development management company specialized in downtown regeneration projects and adaptive use of old big textile factories.

We just have selected our new logo in a pixelbazaar competition and now we are searching for the best stationary design. We expect to receive proposals for:

Two sided business cards
A4 main letterhead
A4 simple text papper
A4 and A5 envelops
A4 single folder front page

information for the stationary project

company signature: FormaCrescimentoDireção (as in the logo files attached)

Business card information: 
Tomás Vieira Lobato FRICS
Managing Director

email: tomas@verticesolar-exemplo.pt
website: www.verticesolar-exemplo.pt

adress: 
R. das Camélias, 83 - 2º
4050-217 Porto

office number
+(351) 22 418 76 53
fax number
+(351) 22 418 76 59
mobile
+(351) 934 207 615

Target Market(s)

professional finantial fund managers and big property owners

Industry/Entity Type

Business

Requirements
Must have
• the company logo

Nice to have
• clear simple contemporary design is appreciated

```html
<!DOCTYPE html>
<html lang="pt">
<head>
<meta charset="utf-8">
<title>Vértice Solar — Stationery</title>
<link href="https://fonts.googleapis.com/css2?family=Source+Sans+3:wght@400;600;700&display=swap" rel="stylesheet">
<style>
  :root {
    --brand-blue: #3d6eb4;
    --line-blue: #8fa6cf;
    --ink-grey: #5a5f66;
    --paper: #ffffff;
    --backdrop: #ecebe8;
    --edge: #d6d6d6;
  }
  * { margin: 0; padding: 0; box-sizing: border-box; }
  html, body { width: 1200px; height: 960px; overflow: hidden; }
  body {
    position: relative;
    background: var(--backdrop);
    font-family: "Source Sans 3", Arial, sans-serif;
    color: var(--ink-grey);
  }
  .sheet {
    position: absolute;
    background: var(--paper);
    border: 1px solid var(--edge);
  }
  .brand { text-align: center; color: var(--brand-blue); font-weight: 700; line-height: 1; white-space: nowrap; }
  .brand-dot { display: block; margin: 0 auto; border-radius: 50%; background: var(--brand-blue); }
  .band {
    position: absolute; background: var(--brand-blue); color: #fff;
    white-space: nowrap; overflow: hidden;
  }
  .rule { position: absolute; height: 1px; background: var(--line-blue); }
  .small { position: absolute; white-space: nowrap; }

  /* Letterhead */
  .letterhead { left: 16px; top: 45px; width: 606px; height: 859px; }
  .letterhead .brand-block { position: absolute; right: 20px; top: 14px; width: 180px; }
  .letterhead .brand { font-size: 26px; }
  .letterhead .brand-dot { width: 28px; height: 28px; margin-bottom: 8px; }
  .letterhead .rule { left: 0; right: 20px; top: 77px; }
  .letterhead .web { right: 46px; top: 80px; font-size: 10.5px; }
  .letterhead .band { left: 0; top: 837px; width: 538px; height: 12px; font-size: 10.5px; line-height: 12px; padding-left: 98px; }

  /* Business cards */
  .card-front { left: 654px; top: 30px; width: 254px; height: 140px; }
  .card-front .brand-block { position: absolute; left: 0; right: 0; top: 42px; }
  .card-front .brand { font-size: 21px; }
  .card-front .brand-dot { width: 24px; height: 24px; margin-bottom: 7px; }
  .card-back { left: 924px; top: 30px; width: 254px; height: 140px; }
  .card-back .brand-block { position: absolute; left: 20px; top: 55px; width: 86px; }
  .card-back .brand { font-size: 10.5px; }
  .card-back .brand-dot { width: 12px; height: 12px; margin-bottom: 4px; }
  .card-back .divider { position: absolute; left: 103px; top: 37px; width: 1px; height: 64px; background: var(--line-blue); }
  .card-back .details { position: absolute; left: 108px; top: 35px; font-size: 7px; line-height: 8.4px; white-space: nowrap; }
  .card-back .details .name { color: var(--brand-blue); font-weight: 600; }
  .card-back .details .gap { height: 7px; }
  .card-back .band { left: 0; right: 0; top: 116px; height: 12px; font-size: 7.5px; line-height: 12px; text-align: center; }

  /* Envelopes */
  .flap { position: absolute; display: block; }
  .dl-envelope { left: 660px; top: 227px; width: 522px; height: 234px; border-top: none; }
  .dl-envelope .brand-block { position: absolute; left: 22px; top: 9px; width: 120px; }
  .dl-envelope .brand { font-size: 16px; }
  .dl-envelope .brand-dot { width: 18px; height: 18px; margin-bottom: 5px; }
  .dl-envelope .rule { left: 0; right: 0; top: 50px; }
  .dl-envelope .web { left: 40px; top: 52px; font-size: 6px; }
  .dl-envelope .band { left: 0; right: 0; top: 218px; height: 9px; font-size: 6.4px; line-height: 9px; padding-left: 23px; }

  .open-envelope { left: 554px; top: 570px; width: 253px; height: 367px; border-top: none; }
  .open-envelope .brand-block { position: absolute; left: 12px; top: 9px; width: 90px; }
  .open-envelope .brand { font-size: 12.5px; }
  .open-envelope .brand-dot { width: 14px; height: 14px; margin-bottom: 4px; }
  .open-envelope .rule { left: 12px; right: 0; top: 40px; }
  .open-envelope .web { left: 26px; top: 41px; font-size: 4.5px; }
  .open-envelope .band { left: 0; right: 0; top: 179px; height: 8px; font-size: 4.8px; line-height: 8px; padding-left: 21px; }
  .open-envelope .fold { position: absolute; left: 0; right: 0; top: 188px; height: 1px; background: var(--edge); }

  /* Plain sheet */
  .plain-sheet { left: 872px; top: 502px; width: 308px; height: 434px; }
</style>
</head>
<body>

  <!-- A4 letterhead -->
  <section class="sheet letterhead" aria-label="A4 letterhead">
    <div class="brand-block"><span class="brand-dot"></span><div class="brand">Vértice Solar</div></div>
    <div class="rule"></div>
    <div class="small web">website: www.verticesolar-exemplo.pt</div>
    <div class="band">R. das Camélias, 83 - 2º 4050-217 Porto, Tel. +(351) 22 418 76 53, fax +(351) 22 418 76 59.</div>
  </section>

  <!-- Business card, front -->
  <section class="sheet card-front" aria-label="Business card front">
    <div class="brand-block"><span class="brand-dot"></span><div class="brand">Vértice Solar</div></div>
  </section>

  <!-- Business card, back -->
  <section class="sheet card-back" aria-label="Business card back">
    <div class="brand-block"><span class="brand-dot"></span><div class="brand">Vértice Solar</div></div>
    <div class="divider"></div>
    <div class="details">
      <div>Managing Director</div>
      <div class="name">Tomás Vieira Lobato FRICS</div>
      <div>+(351) 934 207 615</div>
      <div>email: tomas@verticesolar-exemplo.pt</div>
      <div class="gap"></div>
      <div>R. das Camélias, 83 - 2º 4050-217 Porto</div>
      <div>Tel. +(351) 22 418 76 53</div>
      <div>fax +(351) 22 418 76 59</div>
    </div>
    <div class="band">website: www.verticesolar-exemplo.pt</div>
  </section>

  <!-- DL envelope -->
  <svg class="flap" style="left:660px;top:184px" width="522" height="44" viewBox="0 0 522 44" aria-hidden="true">
    <polygon points="2,0 514,0 522,44 0,44" fill="var(--brand-blue)"/>
  </svg>
  <section class="sheet dl-envelope" aria-label="DL envelope">
    <div class="brand-block"><span class="brand-dot"></span><div class="brand">Vértice Solar</div></div>
    <div class="rule"></div>
    <div class="small web">website: www.verticesolar-exemplo.pt</div>
    <div class="band">R. das Camélias, 83 - 2º 4050-217 Porto, Tel. +(351) 22 418 76 53, fax +(351) 22 418 76 59.</div>
  </section>

  <!-- Open envelope with flaps -->
  <svg class="flap" style="left:500px;top:494px" width="362" height="272" viewBox="0 0 362 272" aria-hidden="true">
    <polygon points="61,0 245,0 254,76 54,76" fill="var(--brand-blue)"/>
    <polygon points="54,76 0,98 0,252 54,268" fill="var(--paper)" stroke="var(--edge)"/>
    <polygon points="308,76 362,98 362,252 308,268" fill="var(--paper)" stroke="var(--edge)"/>
  </svg>
  <section class="sheet open-envelope" aria-label="C5 envelope, opened">
    <div class="brand-block"><span class="brand-dot"></span><div class="brand">Vértice Solar</div></div>
    <div class="rule"></div>
    <div class="small web">website: www.verticesolar-exemplo.pt</div>
    <div class="band">R. das Camélias, 83 - 2º 4050-217 Porto, Tel. +(351) 22 418 76 53, fax +(351) 22 418 76 59.</div>
    <div class="fold"></div>
  </section>

  <!-- A4 plain text paper -->
  <section class="sheet plain-sheet" aria-label="A4 plain continuation sheet"></section>

</body>
</html>
```